2 business magazine ads

Ad 1 — Kestrelview Aero LLC

Ad Type: Full Page | 8.5” × 11” + ¼” Bleed
Audience: Builders • Developers • Contractors
Goal: Promote drone-based visual and thermal services for construction and land development.

Headline Options
• See Every Angle. Build with Precision.
• Your Job Site, Elevated.
• Thermal Inspection. Progress Tracking. Mapping Mastery.

Body Copy

Kestrelview Aero LLC provides professional UAS services to builders and developers across Georgia — delivering the clarity, accuracy, and efficiency your projects demand.

• Thermal Inspections – Detect moisture intrusion, heat loss, and electrical issues early.
• Construction Progress Tracking – Aerial documentation from foundation to finish.
• Land Mapping & Survey Support – Orthomosaic mapping, elevation models, and site analytics.

Certified & Compliant: FAA Licensed • NDPCA Level III • Level 1 Thermographer • OSHA 10 Certified

Call to Action

KestrelviewAero.com | (706) ###-#### | Follow @KestrelviewAero

Design Notes
• Visual: crisp aerial of active construction site with thermal overlay or orthomosaic grid.
• Include FAA and certification badges along the bottom bar.
• Clean, modern layout with bold logo and a “technical blue + white” color palette.

Ad 2 — T&M Assurance Partners LLC

Audience: High-Net-Worth Homeowners • Luxury Builders • Contractors
Goal: Showcase boutique-level insurance expertise for property and construction clients.

Headline Options
• Protect What You’ve Built — and What Builds You.
• Boutique Coverage for Extraordinary Homes & Businesses.
• Luxury Homes. Smart Builders. Sound Protection.

Body Copy

T&M Assurance Partners LLC provides custom-tailored coverage for those who build, own, and protect extraordinary properties.

• High-Value Homes & HNW Client Coverage
• Builders Risk & Contractors Liability
• Business Auto • Workers Comp • Property Protection

As an independent boutique agency, we deliver personal service and deep expertise backed by trusted national carriers — helping you secure the future you’ve built.

Call to Action

T&MAssurancePartners.com | Harlow Springs, GA | (706) ###-####

Design Notes
• Visual: luxury home or builder blueprint composite image.
• Tone: refined and trustworthy — navy, white, and gold palette.
• Layout: prominent logo at top or bottom, clean copy zones with ample white space.

Target Market(s)

Luxury home contractors

Industry/Entity Type

Drone thermal inspection and construction progress tracking, HNW insurance provider, Contractor insurance coverage

Requirements
Must have
• kestrelview - vexo altura 7k drone, luxury lake home under construction. T&M - should show luxury lake home in photo ie lake wendabee in Harlow Springs, GA 30719

```html
<!DOCTYPE html>
<html lang="en">
<head>
<meta charset="utf-8">
<title>T&amp;M Assurance Partners – Boutique Coverage</title>
<link href="https://fonts.googleapis.com/css2?family=DM+Serif+Display&family=Outfit:wght@400;500&family=Libre+Baskerville:ital,wght@1,400;1,700&display=swap" rel="stylesheet">
<style>
  :root {
    --stage: #4a4a4a;
    --paper: #f7f7f7;
    --navy: #101437;
    --ink: #1d1f2b;
    --band-navy: #2a3590;
    --gold: #c99a3c;
    --white: #ffffff;
  }
  * { margin: 0; padding: 0; box-sizing: border-box; }
  html, body { width: 1041px; height: 1200px; overflow: hidden; background: var(--stage); }
  .ad {
    position: absolute; left: 57px; top: 0;
    width: 927px; height: 1200px;
    background: linear-gradient(160deg, #ffffff 0%, var(--paper) 45%, #ececec 100%);
    overflow: hidden;
  }
  .hero-photo {
    position: absolute; left: 31px; top: 32px; width: 430px; height: 1131px;
    background: linear-gradient(180deg,
      #4c5f94 0%, #7b86ad 10%, #e9a878 20%, #f2b46c 25%, #5d6d98 30%,
      #3f4a62 38%, #b07a4c 48%, #d89a5a 58%, #7a5a45 66%,
      #4fb7d1 74%, #2e7e9a 82%, #39455f 90%, #24283a 100%);
  }
  .sky-strip {
    position: absolute; left: 842px; top: 32px; width: 85px; height: 241px;
    background: linear-gradient(180deg, #4c5f94 0%, #7d89b0 40%, #e8a584 70%, #4f6396 86%, #3e5388 100%);
  }
  .brand {
    position: absolute; left: 31px; top: 134px; width: 430px;
    display: flex; align-items: center; justify-content: center; gap: 12px;
  }
  .brand-mark { width: 18px; height: 18px; background: var(--white); }
  .brand-name {
    font-family: "Outfit", sans-serif; font-weight: 500;
    font-size: 28px; color: var(--white); letter-spacing: 0.5px;
  }
  .headline {
    position: absolute; left: 507px; top: 31px; width: 330px;
    font-family: "DM Serif Display", serif; font-weight: 400;
    font-size: 44px; line-height: 53px; color: var(--navy);
  }
  .intro {
    position: absolute; left: 507px; top: 312px; width: 380px;
    font-family: "Outfit", sans-serif; font-size: 20.5px; line-height: 29px; color: var(--ink);
  }
  .services { position: absolute; left: 501px; top: 465px; list-style: none; }
  .service { position: absolute; left: 0; width: 380px; height: 66px; display: flex; align-items: center; }
  .service-icon { width: 66px; height: 66px; flex: none; }
  .service-label {
    margin-left: 11px; font-family: "Outfit", sans-serif; font-size: 19.5px; line-height: 25px; color: var(--ink);
  }
  .closing {
    position: absolute; left: 507px; top: 878px; width: 380px;
    font-family: "Libre Baskerville", serif; font-style: italic; font-weight: 700;
    font-size: 18.5px; line-height: 25.5px; color: var(--navy);
  }
  .contact-bar {
    position: absolute; left: 103px; top: 1058px; width: 791px; height: 105px;
    background: linear-gradient(90deg, rgba(30,26,140,0.72) 0%, rgba(30,26,140,0.72) 45.4%, var(--band-navy) 45.4%);
    font-family: "Outfit", sans-serif; font-weight: 500; font-size: 19.5px; color: var(--white);
  }
  .contact-item { position: absolute; top: 38px; white-space: nowrap; }
  .contact-web { left: 45px; }
  .contact-phone { left: 380px; }
  .contact-place { left: 586px; }
</style>
</head>
<body>
  <main class="ad">
    <div class="hero-photo" role="img" aria-label="Luxury lake home at dusk with glass walls, warm lit terraces and an infinity pool against mountains"></div>
    <div class="sky-strip" role="img" aria-label="Sunset sky over distant mountains"></div>

    <div class="brand">
      <span class="brand-mark"></span>
      <span class="brand-name">T&amp;M Assurance Partners</span>
    </div>

    <h1 class="headline">Boutique Coverage for Extraordinary Homes &amp; Businesses</h1>

    <p class="intro">T&amp;M Assurance Partners LLC provides custom-tailored coverage for those who build, own, and protect extraordinary properties.</p>

    <svg width="0" height="0" style="position:absolute">
      <defs>
        <radialGradient id="goldCoin" cx="35%" cy="30%" r="75%">
          <stop offset="0%" stop-color="#f3d58a"/>
          <stop offset="60%" stop-color="#c99a3c"/>
          <stop offset="100%" stop-color="#8a6420"/>
        </radialGradient>
      </defs>
    </svg>

    <ul class="services">
      <li class="service" style="top:0">
        <svg class="service-icon" viewBox="0 0 66 66"><circle cx="33" cy="33" r="32" fill="url(#goldCoin)"/><g fill="none" stroke="#2a2110" stroke-width="1.6"><rect x="20" y="26" width="10" height="22"/><rect x="30" y="20" width="9" height="28"/><rect x="39" y="28" width="8" height="20"/><line x1="17" y1="48" x2="50" y2="48"/></g></svg>
        <span class="service-label">High-Value Homes &amp; HNW<br>Client Coverage</span>
      </li>
      <li class="service" style="top:77px">
        <svg class="service-icon" viewBox="0 0 66 66"><circle cx="33" cy="33" r="32" fill="url(#goldCoin)"/><g fill="none" stroke="#2a2110" stroke-width="1.6"><circle cx="33" cy="24" r="7"/><path d="M18 40 l8 -6 h14 l8 6 l-8 7 h-14 z"/></g></svg>
        <span class="service-label">Builders Risk &amp; Contractors<br>Liability</span>
      </li>
      <li class="service" style="top:154px">
        <svg class="service-icon" viewBox="0 0 66 66"><circle cx="33" cy="33" r="32" fill="url(#goldCoin)"/><g fill="none" stroke="#2a2110" stroke-width="1.6"><path d="M19 36 a14 14 0 0 1 28 0 z"/><line x1="16" y1="36" x2="50" y2="36"/><circle cx="33" cy="44" r="5"/><path d="M44 16 l6 10 h-12 z"/></g></svg>
        <span class="service-label">Business Auto</span>
      </li>
      <li class="service" style="top:233px">
        <svg class="service-icon" viewBox="0 0 66 66"><circle cx="33" cy="33" r="32" fill="url(#goldCoin)"/><g fill="none" stroke="#2a2110" stroke-width="1.6"><path d="M24 30 a9 9 0 0 1 18 0 z"/><line x1="22" y1="30" x2="44" y2="30"/><rect x="24" y="34" width="18" height="14"/></g></svg>
        <span class="service-label">Workers Comp</span>
      </li>
      <li class="service" style="top:312px">
        <svg class="service-icon" viewBox="0 0 66 66"><circle cx="33" cy="33" r="32" fill="url(#goldCoin)"/><g fill="none" stroke="#2a2110" stroke-width="1.6"><path d="M18 26 l8 -3 l8 3 v8 c0 6 -4 9 -8 11 c-4 -2 -8 -5 -8 -11 z"/><path d="M22 33 l3 3 l5 -6"/><rect x="36" y="20" width="12" height="28"/><line x1="16" y1="48" x2="50" y2="48"/></g></svg>
        <span class="service-label">Property Protection</span>
      </li>
    </ul>

    <p class="closing">As an independent boutique agency, we deliver personal service and deep expertise backed by trusted national carriers — helping you secure the future you’ve built.</p>

    <footer class="contact-bar">
      <span class="contact-item contact-web">T&amp;MAssurancePartners.com</span>
      <span class="contact-item contact-phone">706-555-0148</span>
      <span class="contact-item contact-place">Harlow Springs, GA</span>
    </footer>
  </main>
</body>
</html>
```